ambitious event and festival agency from austria needs fresh business card design

A new design is due for the new headquarters and the new challenges. We organize events for different target groups from 16 to 60 years. The design should therefore be straightforward and not confused, so we are open to new colors and the logo may also be changed. In general, however, the most interesting suggestions are the most interesting ones. after this order we are looking for more graphics for partyvelt facebook instagramm homepage etc A new design is due for the new headquarters and the new challenges. We organize events for different target groups from 16 to 60 years. The design should therefore be straightforward and not confused, so we are open to new colors and the logo may also be changed. In general, however, the most interesting suggestions are the most interesting ones. after this order we are looking for more graphics for partyvelt facebook instagramm homepage etc A new design is due for the new headquarters and the new challenges. We organize events for different target groups from 16 to 60 years. The design should therefore be straightforward and not confused, so we are open to new colors and the logo may also be changed. In general, however, the most interesting suggestions are the most interesting ones. after this order we are looking for more graphics for partyvelt facebook instagramm homepage etc

Reason: I am sorry for this decision but i need some more time. No new designs please, there are so many good ones and I will have made a decision in the next 3 days.

Target Market(s)

Industry/Entity Type

Business

Font styles to use
Serif
Sans Serif

Colors

Designer to choose colors to be used in the design.

Requirements
Must have
Nice to have
Should not have

```html
<!DOCTYPE html>
<html lang="en">
<head>
<meta charset="utf-8">
<title>partyvelt business card</title>
<link href="https://fonts.googleapis.com/css2?family=Open+Sans:wght@400;600&display=swap" rel="stylesheet">
<style>
  :root {
    --bg: #2e2e2e;
    --red: #b9283a;
    --red-light: #c3434f;
    --black: #141414;
    --grey: #8a9090;
    --white: #f2f2f2;
  }
  * { margin: 0; padding: 0; box-sizing: border-box; }
  html, body { width: 1200px; height: 900px; overflow: hidden; }
  body {
    background: var(--bg);
    font-family: "Open Sans", Arial, sans-serif;
    display: flex;
    flex-direction: column;
    align-items: center;
    justify-content: center;
    gap: 40px;
  }
  .card {
    position: relative;
    width: 640px;
    height: 366px;
    border-radius: 22px;
    overflow: hidden;
  }
  .card-front {
    background: linear-gradient(120deg, var(--red-light), var(--red));
  }
  .front-wordmark {
    position: absolute;
    right: 60px;
    top: 150px;
    font-size: 54px;
    font-weight: 400;
    color: var(--white);
    letter-spacing: -0.5px;
  }
  .card-back { background: var(--black); }
  .back-wordmark {
    position: absolute;
    right: 36px;
    top: 34px;
    font-size: 40px;
    font-weight: 400;
    color: var(--red);
    letter-spacing: -0.5px;
  }
  .identity {
    position: absolute;
    left: 34px;
    top: 120px;
    padding-left: 16px;
    border-left: 9px solid var(--red);
  }
  .identity-name { font-size: 22px; color: var(--grey); line-height: 1.15; }
  .identity-title { font-size: 15px; color: var(--red); }
  .contacts {
    position: absolute;
    left: 36px;
    bottom: 32px;
    list-style: none;
    font-size: 15px;
    color: var(--grey);
  }
  .contacts li { display: flex; align-items: center; gap: 10px; height: 26px; }
  .contacts svg { width: 16px; height: 16px; fill: var(--red); }
  .accent-line {
    position: absolute;
    left: 230px;
    right: 0;
    bottom: 52px;
    height: 2px;
    background: var(--red);
  }
  .social {
    position: absolute;
    right: 30px;
    bottom: 64px;
    display: flex;
    align-items: center;
    gap: 6px;
    font-size: 15px;
    color: var(--grey);
  }
  .social-mark { width: 14px; height: 14px; background: var(--red); border-radius: 2px; }
  .social-handle { margin-left: 4px; }
</style>
</head>
<body>
  <section class="card card-front">
    <div class="front-wordmark">partyvelt</div>
  </section>

  <section class="card card-back">
    <div class="back-wordmark">partyvelt</div>

    <div class="identity">
      <div class="identity-name">Your Name</div>
      <div class="identity-title">Job Title</div>
    </div>

    <ul class="contacts">
      <li>
        <svg viewBox="0 0 16 16" aria-hidden="true"><path d="M1 3h14v10H1z M1 3l7 6 7-6" fill="var(--red)"/><path d="M1.5 3.5l6.5 5.5 6.5-5.5" stroke="#141414" stroke-width="1.2" fill="none"/></svg>
        youremail@xyz.com
      </li>
      <li>
        <svg viewBox="0 0 16 16" aria-hidden="true"><path d="M1 5c0-2 3-3 7-3s7 1 7 3v1h-3V4.5H4V6H1z"/><path d="M3 7h10l1 6H2z"/><circle cx="8" cy="10" r="1.6" fill="#141414"/></svg>
        000 000 0000
      </li>
      <li>
        <svg viewBox="0 0 16 16" aria-hidden="true"><circle cx="8" cy="8" r="6.5" fill="none" stroke="var(--red)" stroke-width="1.2"/><ellipse cx="8" cy="8" rx="2.8" ry="6.5" fill="none" stroke="var(--red)" stroke-width="1"/><path d="M1.5 8h13M2.5 5h11M2.5 11h11" stroke="var(--red)" stroke-width="1"/></svg>
        yourwebsite.com
      </li>
    </ul>

    <div class="accent-line"></div>

    <div class="social">
      <span class="social-mark"></span>
      <span class="social-mark"></span>
      <span class="social-handle">/partyvelt</span>
    </div>
  </section>
</body>
</html>
```